依頼詳細
●当社ホームページhttp://tmrv-example.jp/をご覧頂くと、現在の総合カタログNO.50の表紙がご覧になれます。HP内のコンテンツは使って下さっても構いませんが、今までとは違ったものを期待しています。シンプルかつ落ち着いていて、さらには豪華に見えるものを希望します。当社は造花でも特に仏花など宗教造花の割合が多目です。しかしデザインは宗教造花にこだわらないようにしてください。ステキな作品の応募をお待ちしております。

●表裏のデザインですが、裏表紙はデザインの都合で無地でも構いません。背表紙はありません。

●今回は52号です。表表紙のどこかに号数をお入れください。

A4
4ページ
補足説明
●ページ数の欄が4ページとなっています。ポルタミクさんの入力方式でカタログ・パンフレットを選択した場合4ページ以上の選択しかできないためです。実際は表ページのみ1ページ、もしくは表裏ページの2ぺージです。
●50号の表裏表紙のデザインは添付ファイルをご覧ください。当社のロゴと社名、住所はこちらで入れます。
●繰り返しますがお願いするのは表裏表紙のみです。
■ 選んだ理由

1作品目は、ステンドグラス風に加工した、今まで当社のカタログにない斬新な
イメージで、選びました。
2作品目は、蝶が舞うお花畑のようなイメージで、やさしさが伝わってくる感じで選びました。

■ 提案者全員のお礼・コメント

この度は、フラワーカタログ表紙デザインに多数の御提案を頂き、誠にありがとうございました。
どれも素晴らしい作品ばかりで、当社のキャッチフレーズを随所に使用した作品や、斬新なデザイン、複数の御提案を頂いた方、一人一人の思いが込められており、選考に時間がかかりました。
社内で、厳選なる審査の結果、1作品を選ぶ予定でしたが、今回は、2名様の当選としました。
今回残念ながら、当選されなかった方々には、込められた思いに応えることが
出来ず、大変申し訳なく思っております。
ぜひ次の機会にもご提案いただければ幸いです。

```html
<!DOCTYPE html>
<html lang="ja">
<head>
<meta charset="utf-8">
<title>FLOWER CATALOG vol.52</title>
<link rel="stylesheet" href="https://fonts.googleapis.com/css2?family=Cormorant+Garamond:wght@400;500&family=Shippori+Mincho:wght@400&display=swap">
<style>
  :root {
    --paper: #ffffff;
    --ink: #3c3a3a;
    --issue: #d2575a;
    --leaf: #9cc24a;
    --leaf-mid: #c6de8a;
    --leaf-soft: #e9f2cc;
    --blossom: #ef8f8c;
    --blossom-mid: #f6b8ae;
    --blossom-soft: #fbe0d9;
    --peach: #f5bd8c;
    --coral: #e9673f;
    --lemon: #f6e08a;
    --mint: #bfdcae;
  }
  * { margin: 0; padding: 0; box-sizing: border-box; }
  html, body { width: 850px; height: 1200px; overflow: hidden; background: var(--paper); }
  .cover { position: relative; width: 850px; height: 1200px; overflow: hidden; background: var(--paper); }

  .flourish { position: absolute; left: 57px; width: 425px; border-radius: 46% / 50%;
    background:
      radial-gradient(ellipse 30% 40% at 50% 50%, var(--leaf) 0%, rgba(156,194,74,0) 100%),
      radial-gradient(ellipse 48% 46% at 50% 50%, var(--leaf-mid) 0%, var(--leaf-soft) 55%, rgba(255,255,255,0) 100%); }
  .flourish--top { top: 66px; height: 148px; }
  .flourish--bottom { top: 356px; height: 152px; }

  .title { position: absolute; left: 57px; top: 258px; width: 425px; text-align: center;
    font-family: "Cormorant Garamond", serif; font-weight: 400; color: var(--ink); }
  .title__name { display: block; font-size: 40px; letter-spacing: 4px; line-height: 1; }
  .title__issue { display: block; margin-top: 8px; font-size: 46px; font-weight: 500; color: var(--issue); line-height: 1; }

  .tagline { position: absolute; left: 60px; top: 582px;
    font-family: "Shippori Mincho", serif; font-size: 26px; letter-spacing: 7px; color: var(--ink); }
  .tagline rt { font-size: 10px; letter-spacing: 2px; }

  .artwork { position: absolute; }
  .artwork--butterflies { right: 0; top: 0; width: 400px; height: 560px;
    background:
      radial-gradient(ellipse 70px 80px at 290px 130px, var(--lemon) 0%, rgba(246,224,138,.6) 45%, rgba(255,255,255,0) 100%),
      radial-gradient(ellipse 55px 60px at 80px 55px, var(--mint) 0%, rgba(191,220,174,0) 100%),
      radial-gradient(ellipse 36px 30px at 375px 345px, var(--blossom-mid) 0%, rgba(246,184,174,0) 100%),
      radial-gradient(ellipse 50px 45px at 135px 505px, var(--blossom) 0%, rgba(239,143,140,0) 100%); }
  .artwork--garden { left: 0; bottom: 0; width: 850px; height: 830px;
    background:
      radial-gradient(ellipse 55px 55px at 765px 80px, var(--blossom) 0%, var(--blossom-mid) 50%, rgba(246,184,174,0) 100%),
      radial-gradient(ellipse 95px 75px at 705px 255px, var(--coral) 0%, var(--peach) 55%, rgba(245,189,140,0) 100%),
      radial-gradient(ellipse 150px 110px at 720px 480px, var(--blossom) 0%, var(--blossom-mid) 45%, rgba(251,224,217,0) 100%),
      radial-gradient(ellipse 95px 85px at 520px 650px, var(--peach) 0%, var(--blossom-soft) 55%, rgba(251,224,217,0) 100%),
      radial-gradient(ellipse 150px 150px at 330px 470px, var(--blossom) 0%, var(--blossom-mid) 40%, var(--blossom-soft) 70%, rgba(251,224,217,0) 100%),
      radial-gradient(ellipse 45px 45px at 530px 165px, var(--coral) 0%, rgba(233,103,63,0) 100%),
      radial-gradient(ellipse 110px 180px at 810px 370px, var(--mint) 0%, rgba(191,220,174,0) 100%),
      radial-gradient(ellipse 200px 130px at 120px 720px, var(--peach) 0%, var(--blossom-soft) 55%, rgba(251,224,217,0) 100%),
      radial-gradient(ellipse 260px 120px at 600px 800px, var(--mint) 0%, rgba(191,220,174,0) 100%),
      radial-gradient(ellipse 480px 420px at 420px 560px, var(--blossom-soft) 0%, rgba(251,224,217,0) 100%); }
</style>
</head>
<body>
<main class="cover">
  <div class="artwork artwork--garden" role="img" aria-label="ピンクのユリ、ふわふわしたピンクの花、橙の花と緑の葉、舞う蝶が広がる水彩の花畑イラスト"></div>
  <div class="artwork artwork--butterflies" role="img" aria-label="淡い黄色や緑、ピンクの蝶が舞う水彩イラスト"></div>

  <div class="flourish flourish--top" role="img" aria-label="黄緑の唐草模様の飾り"></div>
  <h1 class="title">
    <span class="title__name">FLOWER CATALOG</span>
    <span class="title__issue">vol.52</span>
  </h1>
  <div class="flourish flourish--bottom" role="img" aria-label="黄緑の唐草模様の飾り"></div>

  <p class="tagline">大切な<ruby>瞬間<rt>とき</rt></ruby>に彩りを</p>
</main>
</body>
</html>
```